Business card design needed

We are a boutique law firm within the Melbourne CBD.

You will need to upload our company logo which is to go on the left hand side of the business card - we then have a Bar Collegium of Tarnwell logo to go perhaps on the bottom right hand side (color)

On the back we would like the website details

www.marlowessolicitors.com.au - with a small logo
Updates

Thank you designers for all your great submissions.  Just going through the designs and we will choose one within the next couple of days.

Kind Regards
Marlowes Solicitors Pty Ltd

Industry/Entity Type

Boutique

Contact Information for Business Card

Dermot Marlowe
Principal
Level 6, 47 Quarry Lane
Melbourne VIC Australia 3000
T+61 3 9620 2088 F+61 3 9629 3938
dermot@marlowessolicitors.com.au
M 0491 570 156

```html
<!DOCTYPE html>
<html lang="en">
<head>
<meta charset="utf-8">
<title>Marlowes Solicitors – Business Card</title>
<link href="https://fonts.googleapis.com/css2?family=Arimo:wght@400;700&display=swap" rel="stylesheet">
<style>
  :root {
    --page: #ffffff;
    --ink: #0a0a0a;
    --card-black: #070707;
    --paper: #ffffff;
    --white: #ffffff;
    --photo-dark: #0d0d0d;
    --photo-mid: #3a3a3a;
    --photo-light: #8a8a8a;
    --badge: #9a9a9a;
    --shadow: rgba(0, 0, 0, 0.45);
  }
  * { margin: 0; padding: 0; box-sizing: border-box; }
  html, body {
    width: 1200px; height: 1000px; overflow: hidden;
    background: var(--page);
    font-family: "Arimo", Arial, sans-serif;
  }
  .canvas { position: relative; width: 1200px; height: 1000px; }

  .card {
    position: absolute; left: 350px; width: 500px;
    box-shadow: 3px 4px 5px var(--shadow);
    overflow: hidden;
  }

  /* Front */
  .card-front { top: 172px; height: 292px; background: var(--card-black); color: var(--white); }
  .night-photo {
    position: absolute; left: 0; top: 0; width: 500px; height: 172px;
    background:
      radial-gradient(ellipse 200px 60px at 330px 115px, var(--photo-light) 0%, var(--photo-mid) 45%, transparent 100%),
      linear-gradient(180deg, var(--photo-dark) 0%, #1c1c1c 60%, var(--card-black) 100%);
  }
  .brand { position: absolute; left: 0; top: 4px; display: flex; align-items: flex-end; gap: 8px; }
  .brand-square { width: 54px; height: 54px; background: var(--white); }
  .brand-name { font-weight: 700; font-size: 27px; line-height: 1; letter-spacing: -0.5px; margin-bottom: 1px; }

  .contact-list { position: absolute; left: 51px; top: 128px; font-size: 12px; line-height: 17.6px; }
  .contact-row { display: flex; }
  .contact-label { width: 30px; font-weight: 700; }
  .signature { position: absolute; left: 51px; top: 217px; font-size: 12px; line-height: 18px; }

  .association-badge {
    position: absolute; left: 410px; top: 194px; width: 56px; height: 58px;
    background: radial-gradient(circle at 50% 45%, var(--badge) 0%, #4a4a4a 60%, var(--card-black) 100%);
    border-radius: 6px 6px 28px 28px;
  }

  /* Back */
  .card-back { top: 517px; height: 288px; background: var(--paper); }
  .web-address {
    position: absolute; left: 0; right: 0; top: 117px; text-align: center;
    font-size: 12px; font-weight: 700; color: var(--ink);
  }
  .pointer-icon { position: absolute; left: 363px; top: 125px; }
  .back-band {
    position: absolute; left: 0; bottom: 0; width: 500px; height: 53px;
    background: var(--card-black); display: flex; align-items: center; justify-content: center;
  }
  .brand-small { display: flex; align-items: flex-end; gap: 4px; color: var(--white); margin-top: 6px; }
  .brand-small .brand-square { width: 24px; height: 24px; }
  .brand-small .brand-name { font-size: 14px; margin-bottom: 0; }
</style>
</head>
<body>
<div class="canvas">

  <section class="card card-front">
    <div class="night-photo" role="img" aria-label="Blurred night-time photograph of a lit city building"></div>

    <div class="brand">
      <div class="brand-square"></div>
      <span class="brand-name">Marlowes</span>
    </div>

    <div class="contact-list">
      <div class="contact-row"><span class="contact-label">T</span><span>+61 3 9555 0147</span></div>
      <div class="contact-row"><span class="contact-label">F</span><span>+61 3 9555 0382</span></div>
      <div class="contact-row"><span class="contact-label">E</span><span>dermot@marlowessolicitors.com.au</span></div>
      <div class="contact-row"><span class="contact-label">M</span><span>0491 570 156</span></div>
    </div>

    <div class="signature">
      <p>Dermot Marlowe Principal Marlowes Solicitors Pty Ltd</p>
      <p>Level 6, 47 Quarry Lane Melbourne VIC Australia 3000</p>
    </div>

    <div class="association-badge" role="img" aria-label="Bar Collegium of Tarnwell membership badge"></div>
  </section>

  <section class="card card-back">
    <p class="web-address">http://www.marlowessolicitors.com.au/</p>
    <svg class="pointer-icon" width="12" height="17" viewBox="0 0 12 17" aria-hidden="true">
      <path d="M1 1 L1 14 L4 11 L6.5 16 L8.5 15 L6 10 L10.5 10 Z" fill="#fff" stroke="#000" stroke-width="1" stroke-linejoin="round"/>
    </svg>
    <div class="back-band">
      <div class="brand-small">
        <div class="brand-square"></div>
        <span class="brand-name">Marlowes</span>
      </div>
    </div>
  </section>

</div>
</body>
</html>
```